SOS! The Thistle cafe is in need of a menu face lift!

We need a standout looking menu for our evolving cafe. Our business has grown greatly from our fresh and changing menu, however the menu (look) itself isn't inspiring and is basic.
I have attached some photos of the business and menus I like the look of.
I am open to other ideas (this is why I need your creative help)
Our menu is currently on an A5 clip board, however we are willing to change it a different size if needed.

Would love to have it a multi function eg, used as a takeaway menu as well, possibly bi-fold? Added Wednesday, June 8, 2016

• It would be cool to have some old sea/ pirate references?

```html
<!DOCTYPE html>
<html lang="en">
<head>
<meta charset="utf-8">
<title>The Thistle — Coffee Bar &amp; Grill Menu</title>
<link rel="stylesheet" href="https://fonts.googleapis.com/css2?family=Kaushan+Script&family=Fredoka:wght@400;500&family=Source+Code+Pro:wght@400;600&display=swap">
<style>
  :root {
    --teal: #2bb2a4;
    --teal-deep: #1f9c90;
    --teal-soft: #49c3b6;
    --cream: #f4f0e7;
    --cream-edge: #e7e1d3;
    --ink-teal: #23a396;
    --ink-grey: #8e958f;
    --white: #ffffff;
    --backdrop: #e6e1d7;
  }
  * { box-sizing: border-box; margin: 0; padding: 0; }
  html, body { width: 1200px; height: 943px; overflow: hidden; }
  body {
    background: var(--backdrop);
    font-family: "Source Code Pro", monospace;
    display: flex; align-items: center; justify-content: center; gap: 40px;
  }
  .spread { display: flex; box-shadow: 0 6px 22px rgba(0,0,0,.12); }
  .panel { width: 224px; height: 600px; padding: 24px 16px; position: relative; overflow: hidden; }
  .panel + .panel { border-left: 1px solid rgba(0,0,0,.06); }
  .panel--cream { background: var(--cream); color: var(--ink-grey); }
  .panel--teal { background: var(--teal); color: var(--white); }

  .script-title { font-family: "Kaushan Script", cursive; font-weight: 400; font-size: 34px; line-height: 1; text-align: center; }
  .script-title--small { font-size: 30px; margin-top: 12px; }
  .panel--cream .script-title { color: var(--ink-teal); }
  .subtitle { font-size: 6px; text-align: center; letter-spacing: .5px; text-transform: uppercase; margin-top: 3px; }
  .panel--cream .subtitle { color: var(--ink-teal); }
  .rule { height: 3px; width: 110px; margin: 6px auto 14px; border-radius: 2px; background: currentColor; opacity: .85; }
  .panel--cream .rule { background: var(--ink-teal); }

  .section-head { font-size: 11px; font-weight: 600; letter-spacing: 1px; margin: 12px 0 6px; }
  .panel--cream .section-head { color: var(--ink-teal); }
  .item-list { list-style: none; font-size: 7px; line-height: 1.4; }
  .item-list li { margin-bottom: 5px; }
  .item-list--after-art { margin-top: 14px; }
  .price { color: var(--ink-teal); font-weight: 600; }
  .panel--teal .price { color: var(--white); }

  /* drinks panel */
  .leaf-art { position: absolute; top: 0; left: 0; width: 100%; height: 70px; background: linear-gradient(160deg, var(--teal) 0%, var(--teal-soft) 60%, var(--cream) 100%); }
  .size-tag { display: inline-block; background: var(--teal); color: var(--white); font-size: 7px; padding: 4px 8px; margin-top: 60px; }

  /* cover */
  .cover { display: flex; flex-direction: column; align-items: center; padding: 0; }
  .brand { margin-top: 96px; display: flex; flex-direction: column; align-items: center; gap: 4px; }
  .brand-mark { width: 12px; height: 12px; border-radius: 50%; background: var(--white); }
  .brand-name { font-size: 15px; letter-spacing: 1px; text-transform: uppercase; color: var(--white); }
  .brand-line { font-size: 6px; letter-spacing: 1.5px; text-transform: uppercase; color: var(--white); }
  .title-band { margin-top: 70px; width: 100%; background: var(--cream); padding: 16px 0 12px; text-align: center; }
  .title-band h1 { font-family: "Fredoka", sans-serif; font-weight: 500; font-size: 64px; line-height: 1; color: var(--teal); letter-spacing: 1px; }
  .notice { margin-top: 70px; width: 156px; border: 2px solid var(--white); padding: 20px 14px 18px; position: relative; }
  .notice h2 { position: absolute; top: -12px; left: 50%; transform: translateX(-50%); background: var(--teal); padding: 0 6px; font-family: "Kaushan Script", cursive; font-weight: 400; font-size: 14px; white-space: nowrap; }
  .notice p { font-family: "Fredoka", sans-serif; font-size: 7.5px; line-height: 1.35; }

  /* breakfast */
  .egg-art { width: 64px; height: 52px; border-radius: 8px; margin: 16px auto 0; background: linear-gradient(180deg, var(--white) 0%, var(--cream-edge) 100%); }

  .sub-head { font-size: 11px; letter-spacing: 1.5px; margin: 10px 0 6px; }
  .sandwich-note { font-size: 5.5px; text-align: center; margin-top: 3px; }
</style>
</head>
<body>

<section class="spread spread--outside">
  <article class="panel panel--cream drinks">
    <div class="leaf-art" role="img" aria-label="Palm leaf illustration"></div>
    <span class="size-tag">Cup $3.5 | Mug $4.5</span>
    <h3 class="section-head">hot drinks</h3>
    <ul class="item-list">
      <li>espresso / macchiato / piccolo</li>
      <li>flat white / latte / cappuccino</li>
      <li>mocha / chai / hot chocolate</li>
      <li>tea (ask for range) <span class="price">$3.5</span></li>
    </ul>
    <h3 class="section-head">cold drinks</h3>
    <ul class="item-list">
      <li>iced coffee <span class="price">$5.5</span></li>
      <li>iced chocolate <span class="price">$5.5</span></li>
      <li>iced mocha <span class="price">$6.0</span></li>
      <li>milkshake <span class="price">$5.5</span></li>
      <li>smoothie (berry/banana) <span class="price">$6.5</span></li>
      <li>frappe <span class="price">$6.0</span></li>
      <li>fresh juice <span class="price">$5.5</span></li>
      <li>soft drink can <span class="price">$3.0</span></li>
      <li>bottled water <span class="price">$2.5</span></li>
    </ul>
  </article>

  <article class="panel panel--teal cover">
    <div class="brand">
      <span class="brand-mark"></span>
      <span class="brand-name">The Thistle</span>
      <span class="brand-line">Coffee Bar &amp; Grill</span>
    </div>
    <div class="title-band"><h1>MENU</h1></div>
    <div class="notice">
      <h2>Avast ye!</h2>
      <p>In Pirate terms this means “Pay Attention!” Pay attention to our vast menu. Breakfast, lunch, and dinner all with a wide variety of choices! Take a look at our menu and enjoy!</p>
    </div>
  </article>
</section>

<section class="spread spread--inside">
  <article class="panel panel--cream breakfast">
    <h2 class="script-title">Breakfast</h2>
    <p class="subtitle">All day breakfast menu</p>
    <div class="rule"></div>
    <ul class="item-list">
      <li>toast served buttered w/ jam <span class="price">$5.5</span></li>
      <li>raisin toast w/ butter or cinnamon sugar <span class="price">$6.0</span></li>
      <li>pancakes w/ whipped butter &amp; maple syrup <span class="price">$12.5</span></li>
      <li>granola w/ yoghurt &amp; our own berry compote <span class="price">$11.0</span></li>
      <li>eggs on toast, poached, scrambled or fried <span class="price">$10.0</span></li>
      <li>add a side: bacon, ham, spinach, tomato <span class="price">$3.5</span></li>
    </ul>
    <div class="egg-art" role="img" aria-label="Fried egg illustration"></div>
    <ul class="item-list item-list--after-art">
      <li>eggs benedict w/ ham or bacon <span class="price">$16.5</span></li>
      <li>big breakfast w/ the lot <span class="price">$19.5</span></li>
    </ul>
  </article>

  <article class="panel panel--teal kids">
    <h2 class="script-title">Kids</h2>
    <div class="rule"></div>
    <h3 class="sub-head">breakfast</h3>
    <ul class="item-list">
      <li>egg on toast - poached / scrambled or fried - $5.5</li>
      <li>mini bacon &amp; egg on toast - $7.5</li>
    </ul>
    <h3 class="sub-head">lunch</h3>
    <ul class="item-list">
      <li>nuggets &amp; chips (6 chicken nuggets w/ a bowl of chips &amp; your choice of sauce) - $8.5</li>
      <li>ham &amp; pineapple melt - $6.0</li>
      <li>nachos (corn chips topped w/ our salsa, tasty cheese &amp; sour cream) - $7.5</li>
      <li>babycino - $1.0</li>
      <li>kids drink (see in fridge)</li>
      <li>kids milkshake - $3.5</li>
      <li>single pancake w/ maple syrup and ice cream - $6.0</li>
      <li>yeast spread &amp; cheese melt - $5.5</li>
      <li>yoghurt served w our berry compote - $6.5</li>
    </ul>
    <h2 class="script-title script-title--small">Sandwiches</h2>
    <p class="sandwich-note">fresh $6.0 / toasted $6.5 for 3 fillings</p>
    <div class="rule"></div>
    <ul class="item-list">
      <li>hawaiian leg ham, cheese and pineapple</li>
      <li>tropical chicken, cheese and pineapple</li>
      <li>hot leg ham, cheese and tomato</li>
    </ul>
  </article>

  <article class="panel panel--cream lunch">
    <h2 class="script-title">Lunch</h2>
    <p class="subtitle">served 11am till 3pm</p>
    <div class="rule"></div>
    <h3 class="section-head">wraps</h3>
    <ul class="item-list">
      <li>chicken, bacon, lettuce &amp; aioli <span class="price">$14.5</span></li>
      <li>falafel, hummus, tomato &amp; spinach <span class="price">$13.5</span></li>
    </ul>
    <h3 class="section-head">burgers</h3>
    <ul class="item-list">
      <li>beef, cheese, lettuce, tomato &amp; relish <span class="price">$16.5</span></li>
      <li>crispy chicken w/ slaw &amp; mayo <span class="price">$16.5</span></li>
      <li>veggie patty w/ beetroot &amp; salad <span class="price">$15.5</span></li>
    </ul>
    <h3 class="section-head">house made chicken schnitzels</h3>
    <ul class="item-list">
      <li>served w/ chips &amp; salad <span class="price">$19.5</span></li>
      <li>parmigiana w/ ham &amp; napoli <span class="price">$22.5</span></li>
      <li>topped w/ mushroom sauce <span class="price">$21.5</span></li>
    </ul>
    <h3 class="section-head">Salads</h3>
    <ul class="item-list">
      <li>chicken caesar w/ bacon &amp; egg <span class="price">$17.5</span></li>
      <li>prawn &amp; avocado w/ lemon dressing <span class="price">$18.5</span></li>
    </ul>
  </article>
</section>

</body>
</html>
```